Business card design only (Have Logo Online) Shoudl be quick and easy for designer

We would like to have a business card design that is in-line with our company logo. Final deliverables should include two EPS extension file. One for the front card design and the other the back-end design. Please also indicate the font style used.

Advisory Pebbles is a social enterprise that focuses on utilizing technology, unique methodologies and international partnerships to provide a one-stop location for economical and dependable IT-related solutions.

Target Market(s)

Micro, small and medium business owners.

Industry/Entity Type

Business

Requirements
Must have
• The business card should incorporate our company logo.
Nice to have
• A little web 2.0 style would be nice but I haven''t decided yet.

```html
<!DOCTYPE html>
<html lang="en">
<head>
<meta charset="utf-8">
<title>Advisory Pebbles – Business Card</title>
<link rel="stylesheet" href="https://fonts.googleapis.com/css2?family=Overpass:wght@700;800&display=swap">
<style>
  :root {
    --ink: #111111;
    --brand-green: #4d8a3e;
    --leaf-light: #c6dc96;
    --wash-strong: #d5e3a6;
    --wash-soft: #f3f7e4;
    --paper: #ffffff;
  }
  * { margin: 0; padding: 0; box-sizing: border-box; }
  html, body {
    width: 1200px;
    height: 777px;
    overflow: hidden;
    background: var(--paper);
  }
  .card {
    position: relative;
    width: 1200px;
    height: 777px;
    overflow: hidden;
    background: radial-gradient(ellipse 120% 110% at 100% 30%, var(--paper) 0%, var(--wash-soft) 45%, var(--wash-strong) 100%);
    font-family: "Overpass", "Helvetica Neue", Arial, sans-serif;
    color: var(--ink);
  }
  .card__panel {
    position: absolute;
    inset: 0;
    width: 1200px;
    height: 777px;
  }
  .card__brand {
    position: absolute;
    left: 722px;
    top: 168px;
    display: flex;
    align-items: center;
    gap: 14px;
  }
  .card__brand-dot {
    width: 34px;
    height: 34px;
    border-radius: 50%;
    background: var(--leaf-light);
  }
  .card__brand-name {
    font-weight: 800;
    font-size: 40px;
    letter-spacing: 0.5px;
    color: var(--brand-green);
    line-height: 1;
  }
  .contact {
    position: absolute;
    left: 48px;
    font-weight: 700;
    font-size: 43px;
    line-height: 1;
    white-space: nowrap;
  }
  .contact__name   { top: 72px; }
  .contact__role   { top: 132px; }
  .contact__street { top: 254px; }
  .contact__region { top: 311px; }
  .contact__postal { top: 371px; }
  .contact__phone  { top: 493px; }
  .contact__web    { top: 612px; }
  .contact__email  { top: 670px; }
</style>
</head>
<body>
  <main class="card">
    <svg class="card__panel" viewBox="0 0 1200 777" aria-hidden="true">
      <path d="M450 0 C440 160 520 330 700 385 C820 420 1000 400 1200 355 L1200 0 Z"
            fill="var(--paper)" stroke="#d9e3c2" stroke-width="2"/>
    </svg>

    <div class="card__brand">
      <span class="card__brand-dot"></span>
      <span class="card__brand-name">Advisory Pebbles</span>
    </div>

    <p class="contact contact__name">Darren Lowe</p>
    <p class="contact contact__role">Founder</p>
    <p class="contact contact__street">4120 Alder Lane</p>
    <p class="contact contact__region">BC Canada</p>
    <p class="contact contact__postal">V6K 2J9</p>
    <p class="contact contact__phone">Cell: 1-604-555-0148</p>
    <p class="contact contact__web">www.advisorypebbles.com</p>
    <p class="contact contact__email">darren.lowe@advisorypebbles.com</p>
  </main>
</body>
</html>
```